K9R Business Cards

Business Cards

Contact Information for Business Card

Company name, owner name, license #s, phone & email

Requirements
Should not have
• mailing address

```html
<!DOCTYPE html>
<html lang="en">
<head>
<meta charset="utf-8">
<title>K9R Business Cards</title>
<link href="https://fonts.googleapis.com/css2?family=Open+Sans:wght@700;800&family=Poppins:wght@400&display=swap" rel="stylesheet">
<style>
  :root {
    --backdrop: #9a9a9a;
    --card-white: #ffffff;
    --brand-blue: #00349b;
    --accent-red: #c60a0a;
    --ink: #111111;
    --photo-light: #eef0f2;
    --photo-dark: #2a2a2e;
  }
  * { margin: 0; padding: 0; box-sizing: border-box; }
  html, body { width: 1093px; height: 1200px; overflow: hidden; background: var(--backdrop); }
  .canvas { position: relative; width: 1093px; height: 1200px; }

  .card {
    position: absolute;
    left: 265px;
    height: 356px;
    background: var(--card-white);
    border-radius: 22px;
    overflow: hidden;
  }
  .card--construction { top: 226px; width: 577px; }
  .card--realty { top: 621px; width: 581px; }

  .card__rule {
    position: absolute; left: 0; right: 0; top: 211px; height: 6px;
    background: var(--accent-red);
  }
  .card__band {
    position: absolute; left: 0; right: 0; top: 217px; bottom: 0;
    background: var(--brand-blue);
  }
  .card__portrait {
    position: absolute; left: 335px; right: 0; top: 14px; height: 203px;
    background: linear-gradient(to bottom, var(--photo-light) 0%, var(--photo-light) 60%, var(--photo-dark) 100%);
  }

  .brand { position: absolute; text-align: center; }
  .brand__name {
    display: block;
    font-family: "Open Sans", sans-serif;
    font-weight: 800;
    color: var(--brand-blue);
    line-height: 1;
    letter-spacing: 2px;
  }
  .brand__division {
    display: block;
    font-family: "Open Sans", sans-serif;
    font-weight: 700;
    color: var(--ink);
    line-height: 1;
  }
  .card--construction .brand { left: 22px; top: 56px; width: 188px; }
  .card--construction .brand__name { font-size: 60px; }
  .card--construction .brand__division { font-size: 23px; margin-top: 6px; }
  .card--realty .brand { left: 25px; top: 52px; width: 203px; }
  .card--realty .brand__name { font-size: 64px; }
  .card--realty .brand__division { font-size: 26px; margin-top: 4px; }

  .contact {
    position: absolute; left: 28px; top: 234px;
    font-family: "Poppins", sans-serif;
    font-size: 17px;
    color: var(--card-white);
    line-height: 21px;
    list-style: none;
  }
  .contact__item { display: flex; align-items: center; gap: 7px; }
  .contact__icon { width: 16px; height: 16px; flex: none; }
  .contact__licenses { margin-top: 12px; }

  .holder {
    position: absolute; top: 283px; right: 32px;
    font-family: "Open Sans", sans-serif;
    font-weight: 700;
    font-size: 22px;
    color: var(--card-white);
    letter-spacing: 0.2px;
  }
</style>
</head>
<body>
<div class="canvas">

  <section class="card card--construction">
    <div class="card__rule"></div>
    <div class="card__band"></div>
    <div class="card__portrait" role="img" aria-label="Head-and-shoulders portrait of the card holder in a dark suit"></div>
    <div class="brand">
      <span class="brand__name">K9R</span>
      <span class="brand__division">CONSTRUCTION</span>
    </div>
    <ul class="contact">
      <li class="contact__item">
        <svg class="contact__icon" viewBox="0 0 24 24" aria-hidden="true"><path fill="#fff" d="M6.6 10.8a15.2 15.2 0 0 0 6.6 6.6l2.2-2.2a1 1 0 0 1 1-.25 11.4 11.4 0 0 0 3.6.57 1 1 0 0 1 1 1V20a1 1 0 0 1-1 1A17 17 0 0 1 3 4a1 1 0 0 1 1-1h3.5a1 1 0 0 1 1 1c0 1.25.2 2.45.57 3.57a1 1 0 0 1-.25 1z"/></svg>
        555-014-2276
      </li>
      <li class="contact__item">
        <svg class="contact__icon" viewBox="0 0 24 24" aria-hidden="true"><path fill="#fff" d="M2 5h20v14H2z"/><path fill="none" stroke="#00349b" stroke-width="1.6" d="M2 5l10 8 10-8M2 19l7-7M22 19l-7-7"/></svg>
        dmercer@mailbox.net
      </li>
      <li class="contact__licenses">Builder Lic. #BC-784512<br>Realtor Lic. #40-2291876</li>
    </ul>
    <p class="holder">DALE MERCER</p>
  </section>

  <section class="card card--realty">
    <div class="card__rule"></div>
    <div class="card__band"></div>
    <div class="card__portrait" role="img" aria-label="Head-and-shoulders portrait of the card holder in a dark suit"></div>
    <div class="brand">
      <span class="brand__name">K9R</span>
      <span class="brand__division">Realty</span>
    </div>
    <ul class="contact">
      <li class="contact__item">
        <svg class="contact__icon" viewBox="0 0 24 24" aria-hidden="true"><path fill="#fff" d="M6.6 10.8a15.2 15.2 0 0 0 6.6 6.6l2.2-2.2a1 1 0 0 1 1-.25 11.4 11.4 0 0 0 3.6.57 1 1 0 0 1 1 1V20a1 1 0 0 1-1 1A17 17 0 0 1 3 4a1 1 0 0 1 1-1h3.5a1 1 0 0 1 1 1c0 1.25.2 2.45.57 3.57a1 1 0 0 1-.25 1z"/></svg>
        555-014-2276
      </li>
      <li class="contact__item">
        <svg class="contact__icon" viewBox="0 0 24 24" aria-hidden="true"><path fill="#fff" d="M2 5h20v14H2z"/><path fill="none" stroke="#00349b" stroke-width="1.6" d="M2 5l10 8 10-8M2 19l7-7M22 19l-7-7"/></svg>
        dmercer@mailbox.net
      </li>
      <li class="contact__licenses">Builder Lic. #BC-784512<br>Realtor Lic. #40-2291876</li>
    </ul>
    <p class="holder">DALE MERCER</p>
  </section>

</div>
</body>
</html>
```